Web design for a relaunch of a technology and knowledge transfer company

Design for the relaunch of an existing website The company specializes in technology and knowledge transfer between companies (and universities). The innovation company (company name) combines many years of experience in technology transfer, innovation management, project management and grant applications. Link: http://www.fortschrittswerkhaus.example The colors of the logo are not very advantageous and can be adjusted a bit. There are currently no picture worlds, these are to be selected by the designer. Abstract motifs are certainly an advantage here (10 motifs). Animated programming could be done (network etc. http://valmeta.brixlane.example/). In this case a suggestion is made, which we convert programming technically. The structure and contents of the existing pages will be adopted and supplemented. The programming will be done with TYPO3 in responsive form (bootstrap). Required are start page, content page and contact page. -------------------------------------------------- ------------------------------ Web design for a relaunch of a company in technology and knowledge transfer Design for the relaunch of an existing website. The company specializes in technology and knowledge transfer between companies (and universities). The innovation company combines many years of experience in the fields of technology transfer, innovation management, project management and grant application. Link: http://www.fortschrittswerkhaus.example The color of the logo is not exactly advantageous and can be adjusted. There are currently no image worlds, these are to be selected by the designer. Abstract motifs are certainly an advantage here (10 motifs). It could also be made animated programming (network, etc. http://valmeta.brixlane.example/). In this case, a proposal has to be made, which we implement in terms of programming technology. The structure and contents of the existing pages are taken over and supplemented. Programming is done with TYPO3 in responsive form (bootstrap). Required are homepage, content page and contact page.

```html
<!DOCTYPE html>
<html lang="en">
<head>
<meta charset="utf-8">
<title>Fortschrittswerkhaus – Technology and Knowledge Transfer</title>
<link href="https://fonts.googleapis.com/css2?family=Lato:wght@400;700&display=swap" rel="stylesheet">
<style>
:root{
  --navy:#1f2470;
  --navy-deep:#141a55;
  --blue:#2f35a0;
  --red:#e3142d;
  --ink:#222;
  --text:#444;
  --muted:#777;
  --line:#dcdcdc;
  --footer:#333333;
  --footer-light:#f1f1f1;
  --white:#fff;
}
*{box-sizing:border-box;margin:0;padding:0}
html,body{width:1200px;height:3879px;overflow:hidden}
body{font-family:"Lato",Arial,sans-serif;color:var(--text);background:var(--white);position:relative}
.abs{position:absolute}
.btn{position:absolute;background:var(--red);color:var(--white);font-size:15px;display:flex;align-items:center;justify-content:center}
h2.section-title{position:absolute;left:0;width:1200px;text-align:center;font-weight:400;font-size:30px;color:var(--ink);letter-spacing:.5px}
.lead{position:absolute;left:290px;width:620px;text-align:center;font-size:14px;line-height:19px;color:var(--text)}

/* header */
.site-header{position:absolute;top:0;left:0;width:1200px;height:114px}
.brand{position:absolute;left:83px;top:20px;display:flex;align-items:center;gap:12px}
.brand-mark{width:34px;height:34px;background:var(--navy)}
.brand-name{font-size:17px;font-weight:700;color:var(--navy);letter-spacing:.5px}
.call{position:absolute;left:957px;top:36px;display:flex;gap:10px;align-items:center;font-size:14px;color:var(--ink);line-height:18px}
.main-nav{position:absolute;top:114px;left:0;width:1200px;height:41px;background:var(--blue);display:flex;align-items:center;padding-left:85px}
.main-nav a{color:var(--white);text-decoration:none;font-size:15px;height:41px;display:flex;align-items:center;justify-content:center}
.main-nav a.active{background:var(--red);width:96px}
.main-nav .search{position:absolute;left:1104px;top:12px}

/* hero */
.hero{position:absolute;top:155px;left:0;width:1200px;height:479px;background:radial-gradient(ellipse at 50% 40%,#3a3f9e 0%,#262b80 45%,var(--navy-deep) 100%)}
.hero h1{position:absolute;top:200px;left:0;width:1200px;text-align:center;color:var(--white);font-size:29px;font-weight:400;line-height:38px}
.hero svg.edge{position:absolute;left:0;bottom:0}

/* intro */
.intro-btn{left:525px;top:822px;width:152px;height:37px}

/* services */
.service{position:absolute;width:298px}
.service .photo{width:298px;height:220px}
.service p{text-align:center;font-size:18px;line-height:24px;color:var(--ink);margin-top:30px;padding:0 40px}

/* references */
.references{position:absolute;top:1699px;left:0;width:1200px;height:442px;background:linear-gradient(100deg,#2b3196 0%,var(--blue) 60%,#3a40b0 100%);color:var(--white)}
.references h3{position:absolute;left:83px;top:76px;font-size:27px;font-weight:400}
.references .copy{position:absolute;left:83px;top:124px;width:470px;font-size:13px;line-height:16px}
.references .copy p{margin-bottom:14px}
.references .btn{left:83px;top:340px;width:147px;height:37px}
.references .frame{position:absolute;left:615px;top:49px;width:502px;height:349px;border:8px solid var(--white);background:linear-gradient(135deg,#0a1630,#143c6e 60%,#0c1a38)}

/* cards */
.card{position:absolute;width:339px;height:387px;background:var(--white);border:1px solid var(--line);box-shadow:0 1px 4px rgba(0,0,0,.08)}
.card .photo{margin:8px;height:207px}
.card .meta{font-size:13px;color:var(--text);padding:0 16px;margin-top:8px}
.card h4{font-size:14px;color:var(--ink);padding:0 16px;margin-top:10px;font-weight:700}
.card .body{font-size:13px;line-height:16px;padding:0 16px;margin-top:6px;color:var(--text)}
.card .more{position:absolute;left:16px;bottom:22px;font-size:12px;display:flex;gap:6px;align-items:center;color:var(--ink)}

/* newsletter */
.newsletter-input{position:absolute;left:318px;top:3414px;width:414px;height:36px;border:1px solid var(--line);font-size:13px;padding:10px 12px;color:var(--muted)}
.newsletter-btn{left:732px;top:3414px;width:152px;height:36px}

/* footer */
.site-footer{position:absolute;top:3512px;left:0;width:1200px;height:310px;background:var(--footer);color:var(--white)}
.footer-about{position:absolute;left:78px;top:0;width:219px;height:310px;background:var(--footer-light);color:var(--ink);padding:50px 18px 0}
.footer-about .brand-name{font-size:14px}
.footer-about p{font-size:13px;line-height:16px;margin-top:26px}
.footer-col{position:absolute;top:66px}
.footer-col h5{font-size:14px;font-weight:700;margin-bottom:26px}
.footer-col li{list-style:none;font-size:13px;line-height:21px}
.footer-col li::before{content:"›";margin-right:10px}
.contact-row{font-size:13px;line-height:22px;display:flex}
.contact-row b{width:28px;font-weight:400}
.qc-field{position:absolute;background:#555;font-size:12px;padding:6px 10px;color:#ddd}
.qc-send{left:846px;top:235px;width:150px;height:36px}
.copyright{position:absolute;top:3822px;left:0;width:1200px;height:57px}
.copyright p{position:absolute;left:100px;top:20px;font-size:13px;color:var(--text)}
.social{position:absolute;left:910px;top:22px;display:flex;gap:22px}
.social span{width:13px;height:13px;border-radius:50%;background:var(--ink)}
</style>
</head>
<body>

<header class="site-header">
  <div class="brand"><span class="brand-mark"></span><span class="brand-name">FORTSCHRITTSWERKHAUS</span></div>
  <div class="call">
    <svg width="26" height="26" viewBox="0 0 26 26"><circle cx="13" cy="13" r="12" fill="none" stroke="#222" stroke-width="1.5"/><path d="M9 7l3 3-2 2c1 2 2 3 4 4l2-2 3 3-2 2c-5 0-10-5-10-10z" fill="#222"/></svg>
    <div>Call Us Now!<br>49 5550 12 34 567</div>
  </div>
</header>

<nav class="main-nav">
  <a class="active" href="#">Home</a>
  <a href="#" style="width:138px">About us</a>
  <a href="#" style="width:94px">Services</a>
  <a href="#" style="width:130px">References</a>
  <a href="#" style="width:170px">Events &amp; Workshops</a>
  <a href="#" style="width:120px">Reports</a>
  <a href="#" style="width:122px">Contact</a>
  <svg class="search" width="16" height="16" viewBox="0 0 16 16"><circle cx="6.5" cy="6.5" r="5" fill="none" stroke="#fff" stroke-width="2"/><path d="M10 10l5 5" stroke="#fff" stroke-width="2"/></svg>
</nav>

<section class="hero" role="img" aria-label="Abstract network of connected points on a deep blue background">
  <h1>Transfer Company That Supports<br>Companies in Implementing Their<br>Innovative Ideas</h1>
  <svg class="abs" style="left:580px;top:318px" width="40" height="40" viewBox="0 0 40 40"><circle cx="20" cy="20" r="17" fill="none" stroke="#fff" stroke-width="3"/><path d="M16 12l11 8-11 8z" fill="#fff"/></svg>
  <svg class="edge" width="1200" height="60" viewBox="0 0 1200 60"><path d="M0 0 L600 52 L1200 0" fill="none" stroke="#6b70c8" stroke-width="3"/><path d="M0 6 L600 60 L1200 6 L1200 60 L0 60Z" fill="#fff"/></svg>
</section>

<h2 class="section-title" style="top:725px">The Innovation Society</h2>
<p class="lead" style="top:774px">is a technology and knowledge transfer company that supports companies in implementing their innovative ideas. We use our large network of scientific institutions.</p>
<a class="btn intro-btn">Read More</a>

<h2 class="section-title" style="top:888px">Services</h2>
<p class="lead" style="top:937px">The innovation company brings together over 15 years of experience in the areas of technology transfer, innovation management, project management and grant application.</p>

<div class="service" style="left:111px;top:1021px"><div class="photo" role="img" aria-label="Hand holding a tablet with a city and technology icons" style="background:linear-gradient(135deg,#1c3a5c,#4f7fa6 50%,#d4dde6)"></div><p>Technology And Knowledge Transfer</p></div>
<div class="service" style="left:447px;top:1021px"><div class="photo" role="img" aria-label="Fingers touching glowing light" style="background:radial-gradient(circle at 55% 50%,#f3c28a,#b85a2a 40%,#2a1a18 85%)"></div><p>Innovation and project management</p></div>
<div class="service" style="left:784px;top:1021px"><div class="photo" role="img" aria-label="Team joining fists over a desk" style="background:linear-gradient(135deg,#8a8278,#c9c3ba 50%,#5c554d)"></div><p>Cooperation and network Management</p></div>
<div class="service" style="left:111px;top:1350px"><div class="photo" role="img" aria-label="Hands signing a document" style="background:linear-gradient(135deg,#3a3631,#9a938a 55%,#e4e0da)"></div><p>Property Rights and Co.</p></div>
<div class="service" style="left:447px;top:1350px"><div class="photo" role="img" aria-label="Open hands holding a glowing light bulb" style="background:radial-gradient(circle at 50% 40%,#9fe3ef,#2b8aa6 45%,#0f3b52)"></div><p>From Ideas To Innovations</p></div>
<div class="service" style="left:784px;top:1350px"><div class="photo" role="img" aria-label="Financial chart with glowing bars" style="background:linear-gradient(135deg,#e7a3c3,#6a7ad6 50%,#1a2f7a)"></div><p>All About Money - Promotion</p></div>

<section class="references">
  <h3>References</h3>
  <div class="copy">
    <p><b>The innovation society for universities and industry is active across all sectors.</b></p>
    <p>Amongst others, our customers come from the fields of mechanical engineering, electrical engineering, packaging technology, special machine construction, drive technology, agricultural machinery engineering, software engineering, medical technology, space energy management, construction, stainless steel processing, but also from the craft trades and the food industry.</p>
    <p>Since we usually have secrecy agreements with our customers, we do not publish any companies here</p>
  </div>
  <a class="btn">Read More</a>
  <div class="frame" role="img" aria-label="Hand holding a glowing digital brain network"></div>
</section>

<h2 class="section-title" style="top:2194px;font-size:27px">Events &amp; Workshops</h2>

<article class="card" style="left:67px;top:2268px"><div class="photo" role="img" aria-label="Event poster with cloud and device illustrations" style="background:linear-gradient(135deg,#2a6fb8,#7fb6e4 60%,#f0a040)"></div><div class="meta">By Admin &nbsp;|&nbsp; 03,April, 2019</div><h4>What is Lorem Ipsum?</h4><p class="body">Lorem Ipsum is simply dummy the printing a typesetting industry. Lorem Ipsum has been the standard dummy.</p><span class="more">Continue.. <svg width="11" height="11" viewBox="0 0 11 11"><circle cx="5.5" cy="5.5" r="5.5" fill="#222"/><path d="M4 3l3 2.5L4 8" stroke="#fff" fill="none"/></svg></span></article>
<article class="card" style="left:434px;top:2268px"><div class="photo" role="img" aria-label="Speaker at a workshop in a conference room" style="background:linear-gradient(135deg,#9a9590,#d8d2c8 55%,#6a6058)"></div><div class="meta">By Admin &nbsp;|&nbsp; 03,April, 2019</div><h4>What is Lorem Ipsum?</h4><p class="body">Lorem Ipsum is simply dummy the printing a typesetting industry. Lorem Ipsum has been the standard dummy.</p><span class="more">Continue.. <svg width="11" height="11" viewBox="0 0 11 11"><circle cx="5.5" cy="5.5" r="5.5" fill="#222"/><path d="M4 3l3 2.5L4 8" stroke="#fff" fill="none"/></svg></span></article>
<article class="card" style="left:802px;top:2268px"><div class="photo" role="img" aria-label="Connected smart city at night" style="background:linear-gradient(135deg,#0c2a55,#2e78b8 55%,#9ed0f0)"></div><div class="meta">By Admin &nbsp;|&nbsp; 03,April, 2019</div><h4>What is Lorem Ipsum?</h4><p class="body">Lorem Ipsum is simply dummy the printing a typesetting industry. Lorem Ipsum has been the standard dummy.</p><span class="more">Continue.. <svg width="11" height="11" viewBox="0 0 11 11"><circle cx="5.5" cy="5.5" r="5.5" fill="#222"/><path d="M4 3l3 2.5L4 8" stroke="#fff" fill="none"/></svg></span></article>

<a class="btn" style="left:525px;top:2692px;width:150px;height:39px">View More</a>

<h2 class="section-title" style="top:2768px;font-size:27px">Reports</h2>

<article class="card" style="left:67px;top:2827px"><div class="photo" style="height:209px;background:linear-gradient(135deg,#4a3c2c,#a08a6a 55%,#2c241a)" role="img" aria-label="Panel discussion at a forum"></div><div class="meta">10.09.2018</div><h4>IoT - what companies want</h4><p class="body">The innovation forum BrightLift initiated at the University of Applied Sciences Northfield / Campus Elmbrook...</p><span class="more">Continue.. <svg width="11" height="11" viewBox="0 0 11 11"><circle cx="5.5" cy="5.5" r="5.5" fill="#222"/><path d="M4 3l3 2.5L4 8" stroke="#fff" fill="none"/></svg></span></article>
<article class="card" style="left:434px;top:2827px"><div class="photo" style="height:209px;background:linear-gradient(135deg,#2c3c5a,#8a9ab4 55%,#3a4660)" role="img" aria-label="Guests talking at a networking event"></div><div class="meta">09/10/2018</div><h4>Innovation transfer for the region</h4><p class="body">Elmbrook (nfu). It formed the conclusion of an intensive phase: the conference "BrightLift" on 5 and 6 September...</p><span class="more">Continue.. <svg width="11" height="11" viewBox="0 0 11 11"><circle cx="5.5" cy="5.5" r="5.5" fill="#222"/><path d="M4 3l3 2.5L4 8" stroke="#fff" fill="none"/></svg></span></article>
<article class="card" style="left:802px;top:2827px"><div class="photo" style="height:209px;background:linear-gradient(135deg,#2a2e3a,#7a8090 55%,#c8ccd4)" role="img" aria-label="Group of representatives standing together"></div><div class="meta">14.02.2018</div><h4>Innovation Society represented</h4><p class="body">The Student Engineering Office Eastmoor has been a good address for years for the processing of student...</p><span class="more">Continue.. <svg width="11" height="11" viewBox="0 0 11 11"><circle cx="5.5" cy="5.5" r="5.5" fill="#222"/><path d="M4 3l3 2.5L4 8" stroke="#fff" fill="none"/></svg></span></article>

<a class="btn" style="left:525px;top:3243px;width:150px;height:39px">View More</a>

<h2 class="section-title" style="top:3338px;font-size:22px">Subscribe To Our Newsletter</h2>
<p class="abs" style="top:3370px;left:0;width:1200px;text-align:center;font-size:14px;color:var(--ink)">To Receive The Latest News &amp; Update</p>
<div class="newsletter-input">Email here</div>
<a class="btn newsletter-btn">Submit</a>

<footer class="site-footer">
  <div class="footer-about">
    <span class="brand-mark" style="display:block;width:30px;height:30px;margin-bottom:10px"></span>
    <span class="brand-name">FORTSCHRITTSWERKHAUS</span>
    <p>Lorem Ipsum is simply dummy text of the printing and type setting industry. Lorem Ipsum has been the industry's</p>
    <p style="margin-top:6px">Read More.. ›</p>
  </div>
  <div class="footer-col" style="left:362px">
    <h5>Quick Link</h5>
    <ul><li>Home</li><li>About us</li><li>Services</li><li>References</li><li>Events &amp; Workshops</li><li>Reports</li><li>Contact</li></ul>
  </div>
  <div class="footer-col" style="left:559px">
    <h5>Contact us</h5>
    <div class="contact-row"><b>A :</b><span>Lindenweg 22<br>30999 Musterfeld</span></div>
    <div class="contact-row"><b>P :</b><span>+49 5550 12 34 567</span></div>
    <div class="contact-row"><b>F :</b><span>+49 5550 12 34 890</span></div>
    <div class="contact-row"><b>E :</b><span>info@fortschrittswerkhaus.example</span></div>
  </div>
  <div class="footer-col" style="left:846px">
    <h5>Quick Contact</h5>
  </div>
  <div class="qc-field" style="left:846px;top:126px;width:130px;height:28px">Name</div>
  <div class="qc-field" style="left:984px;top:126px;width:134px;height:28px">Phone</div>
  <div class="qc-field" style="left:846px;top:162px;width:272px;height:56px">Message</div>
  <a class="btn qc-send">SEND</a>
</footer>

<div class="copyright">
  <p>©Copyright 2019. Fortschrittswerkhaus LLC, All Rights Reserved.</p>
  <div class="social"><span></span><span></span><span></span><span></span><span></span></div>
</div>

</body>
</html>
```